Building Company Business Card Design

Need a design for a business card:
It needs to have: Name, Phone, Facebook link, Website, email
i would also like a list of works we undertake:
-New Homes
-Extensions, Renovations & Bathrooms
-Decking, Carports, Sheds (Residential and Industrial)
-Carpentry
-Fences, Patios & Pergolas

Name, Phone, Facebook link, Website, email + details of services provided listed in description

```html
<!DOCTYPE html>
<html lang="en">
<head>
<meta charset="utf-8">
<title>Ridgeline Homes Business Card</title>
<link rel="stylesheet" href="https://fonts.googleapis.com/css2?family=Montserrat:wght@400;500;700&display=swap">
<style>
  :root {
    --stage: #2d2d2d;
    --card-light: #ffffff;
    --card-dark: #1c1c1c;
    --green: #37b54a;
    --green-tint: #e6f5e6;
    --grey-tint: #efefef;
    --ink: #1a1a1a;
    --grey: #7a7a7a;
    --grey-light: #8d8d8d;
    --white: #ffffff;
  }
  * { box-sizing: border-box; margin: 0; padding: 0; }
  html, body { width: 1200px; height: 1059px; overflow: hidden; }
  body {
    background: var(--stage);
    font-family: "Montserrat", sans-serif;
    position: relative;
  }
  .card {
    position: absolute;
    left: 255px;
    width: 690px;
    height: 392px;
    overflow: hidden;
  }
  .card--front { top: 100px; background: var(--card-light); }
  .card--back { top: 537px; background: var(--card-dark); }

  /* front */
  .front-decor {
    position: absolute;
    right: -60px;
    top: 60px;
    width: 380px;
    height: 380px;
    border-radius: 50%;
    background: linear-gradient(135deg, var(--grey-tint) 0%, var(--green-tint) 100%);
  }
  .wordmark {
    position: absolute;
    display: flex;
    align-items: center;
    gap: 10px;
  }
  .wordmark__square {
    width: 22px; height: 22px;
    background: var(--green);
    flex: none;
  }
  .wordmark__text {
    font-weight: 700;
    line-height: 1.05;
    letter-spacing: 0.5px;
  }
  .wordmark__line2 { display: block; font-size: 0.5em; letter-spacing: 0.3px; }
  .card--front .wordmark { left: 33px; top: 78px; }
  .card--front .wordmark__text { font-size: 30px; color: var(--ink); }

  .name-tab {
    position: absolute; left: 0; top: 187px;
    width: 18px; height: 46px;
    background: var(--green);
    border-radius: 0 4px 4px 0;
  }
  .person { position: absolute; left: 34px; top: 183px; }
  .person__name {
    font-size: 29px; font-weight: 700; color: var(--green); letter-spacing: 1px;
  }
  .person__role {
    font-size: 15.5px; font-weight: 400; color: var(--ink); letter-spacing: 1px; margin-top: 2px;
  }
  .contacts {
    position: absolute; left: 32px; top: 256px;
    list-style: none;
  }
  .contacts li {
    display: flex; align-items: center; gap: 8px;
    height: 26.5px;
    font-size: 16px; color: var(--ink); letter-spacing: 0.4px;
  }
  .contacts svg { width: 14px; height: 14px; flex: none; fill: var(--green); }

  /* back */
  .card--back .wordmark {
    left: 0; right: 0; top: 150px;
    justify-content: center;
  }
  .card--back .wordmark__text { font-size: 40px; color: var(--white); text-align: center; }
  .services {
    position: absolute; left: 0; right: 0; top: 307px;
    text-align: center;
    font-size: 15.5px; color: var(--white); letter-spacing: 0.3px;
    line-height: 26px;
  }
  .services__item { white-space: nowrap; }
  .services__bullet {
    display: inline-block; width: 9px; height: 9px;
    background: var(--green);
    margin: 0 7px 1px 9px;
  }
</style>
</head>
<body>

<section class="card card--front">
  <div class="front-decor" aria-hidden="true"></div>

  <div class="wordmark">
    <span class="wordmark__square"></span>
    <span class="wordmark__text">RIDGELINE HOMES<span class="wordmark__line2">AND DEVELOPMENTS PTY LTD</span></span>
  </div>

  <div class="name-tab"></div>
  <div class="person">
    <p class="person__name">DANIEL BROOKS</p>
    <p class="person__role">MANAGER</p>
  </div>

  <ul class="contacts">
    <li>
      <svg viewBox="0 0 24 24"><path d="M6.6 10.8a15 15 0 0 0 6.6 6.6l2.2-2.2a1 1 0 0 1 1-.25 11.4 11.4 0 0 0 3.6.6 1 1 0 0 1 1 1V20a1 1 0 0 1-1 1A17 17 0 0 1 3 4a1 1 0 0 1 1-1h3.5a1 1 0 0 1 1 1c0 1.25.2 2.45.6 3.6a1 1 0 0 1-.25 1z"/></svg>
      (555)014-2398
    </li>
    <li>
      <svg viewBox="0 0 24 24"><path d="M2 5h20v2l-10 6L2 7zM2 9l10 6 10-6v10H2z"/></svg>
      info@youremail.com
    </li>
    <li>
      <svg viewBox="0 0 24 24"><path d="M12 2a10 10 0 1 0 0 20 10 10 0 0 0 0-20zm0 2c.9 1.2 1.6 2.6 2 4h-4c.4-1.4 1.1-2.8 2-4zM4.3 14a8 8 0 0 1 0-4h3.4a16 16 0 0 0 0 4zm.8 2h3c.4 1.4 1 2.7 1.8 3.8A8 8 0 0 1 5.1 16zm3-8h-3a8 8 0 0 1 4.8-3.8C9.1 5.3 8.5 6.6 8.1 8zM12 20c-.9-1.2-1.6-2.6-2-4h4c-.4 1.4-1.1 2.8-2 4zm2.3-6H9.7a14 14 0 0 1 0-4h4.6a14 14 0 0 1 0 4zm.8 5.8c.8-1.1 1.4-2.4 1.8-3.8h3a8 8 0 0 1-4.8 3.8zM16.3 14a16 16 0 0 0 0-4h3.4a8 8 0 0 1 0 4zm.6-6c-.4-1.4-1-2.7-1.8-3.8A8 8 0 0 1 19.9 8z"/></svg>
      www.yourwebsite.com
    </li>
    <li>
      <svg viewBox="0 0 24 24"><circle cx="12" cy="12" r="10"/></svg>
      @your facebook link
    </li>
  </ul>
</section>

<section class="card card--back">
  <div class="wordmark">
    <span class="wordmark__square"></span>
    <span class="wordmark__text">RIDGELINE HOMES<span class="wordmark__line2">AND DEVELOPMENTS PTY LTD</span></span>
  </div>

  <div class="services">
    <p>
      <span class="services__item"><span class="services__bullet"></span>New Homes</span>
      <span class="services__item"><span class="services__bullet"></span>Extensions, Renovations &amp; Bathrooms</span>
    </p>
    <p>
      <span class="services__item"><span class="services__bullet"></span>Decking, Carports, Sheds</span>
      <span class="services__item"><span class="services__bullet"></span>Carpentry</span>
      <span class="services__item"><span class="services__bullet"></span>Fences, Patios &amp; Pergolas</span>
    </p>
  </div>
</section>

</body>
</html>
```